MARLOWE BRIGHT WORKS WEBSITE HOME PAGE AND CHECKOUT PAGES

UPDATE TO BRIEF:

Marlowe Bright Works is a company that provides Charities with the Free Vacation Vouchers that they can use to incentivize people to donate which in turn increases donations for the chairty.

So I need to keep it a little more template like the example url I gave. http://pagefernly.com/marlowe-bright-work/ Because, I am going to provide template to ANY CHARITY TYPE and they just fill in the content into the template and change images or whatever for their charity. So I am really looking for a website template that can be used for multiple and different kinds of charities.

So where the logo would go please use YOUR LOGO HERE generic logo for now

and where ever you promote the Free Vacation Certificate To Las Vegas please add "Brought To You By" (logo marlowe bright works or something...basically its a partnership with the Charity and Marlowe Bright Work)

So Marlowe Bright Work is a marketing company and not a Charity but more of a plug and play platform that allows a charity to accepts donations and immediately deliver the promised incentive offer after donation is made on the website.

When a Charity is able to offer a high perceived value gift for a donation they increase donations.

Target Market(s)

PEOPLE THAT DONATE TO CHARITIES

Industry/Entity Type

Charity

Number of Pages Required

3 page

Requirements
Must have
• One thing i need to add to the website is an Incentive Gift for the Donation.

So I need this tagline and images to make the promotion seem great:
"Donate $100 and Receive A Free 3 Night Vacation Certificate To Las Vegas!"

Maybe show image of vegas or some kind of nice graphic that promotes the vegas vacation as a gift for the $100 donation very well"

I need the payment pages as well. So when someone click Donate Now, the next page is there where they can see their gift that is included with the donation, and also the donation amount...
Nice to have

Should not have

```html
<!DOCTYPE html>
<html lang="en">
<head>
<meta charset="utf-8">
<title>The Polar Bears – Essential Habitat | Marlowe Bright Works</title>
<link rel="stylesheet" href="https://fonts.googleapis.com/css2?family=Montserrat:wght@400;600;700;800&family=Open+Sans:wght@400;600&display=swap">
<style>
  :root {
    --navy: #1d2a38;
    --navy-deep: #18222e;
    --cyan: #1fb5e8;
    --cyan-soft: #45c3ee;
    --orange: #f47b20;
    --white: #ffffff;
    --text: #6b7480;
    --light: #f4f6f8;
    --rule: #d8dde3;
  }
  * { box-sizing: border-box; margin: 0; padding: 0; }
  html, body { width: 1200px; height: 5100px; overflow: hidden; }
  body { font-family: "Open Sans", Arial, sans-serif; color: var(--text); background: var(--white); }
  section, footer { position: relative; width: 1200px; overflow: hidden; }
  .abs { position: absolute; }
  .heading { font-family: "Montserrat", Arial, sans-serif; color: var(--navy); font-weight: 700; text-transform: uppercase; line-height: 1; }
  .eyebrow { font-family: "Montserrat", Arial, sans-serif; font-size: 13px; font-weight: 700; color: var(--orange); letter-spacing: 1px; text-transform: uppercase; }
  .body-copy { font-size: 14px; line-height: 1.7; color: var(--text); }
  .btn { display: inline-block; background: var(--orange); color: var(--white); font-family: "Montserrat", Arial, sans-serif; font-weight: 700; font-size: 13px; letter-spacing: 1px; text-transform: uppercase; padding: 14px 26px; border-radius: 3px; white-space: nowrap; }
  .photo { border-radius: 50%; }

  /* Hero */
  .hero { height: 640px; background: linear-gradient(180deg, #c9d6e0 0%, #e4ebf1 45%, #f3f6f9 100%); }
  .hero-bear { left: 680px; top: 0; width: 520px; height: 640px; background: radial-gradient(ellipse at 55% 55%, #f4efe4 0%, #e3ddd0 40%, rgba(220,228,236,0) 72%); }
  .brand { left: 64px; top: 40px; display: flex; align-items: center; gap: 10px; font-family: "Montserrat", Arial, sans-serif; font-weight: 700; font-size: 15px; color: var(--navy); }
  .brand-mark { width: 22px; height: 22px; background: var(--cyan); }
  .hero-title { left: 84px; top: 146px; font-size: 86px; font-weight: 800; letter-spacing: 1px; white-space: nowrap; }
  .hero-sub { left: 88px; top: 244px; font-family: "Montserrat", Arial, sans-serif; font-size: 48px; font-weight: 600; color: var(--cyan); text-transform: uppercase; line-height: 1; white-space: nowrap; }
  .hero-line { left: 88px; top: 306px; font-family: "Montserrat", Arial, sans-serif; font-size: 18px; font-weight: 600; color: var(--navy); text-transform: uppercase; white-space: nowrap; }
  .hero .btn { left: 88px; top: 366px; }

  /* Vegas offer */
  .offer { height: 500px; }
  .offer-copy { left: 64px; top: 108px; width: 460px; }
  .offer-l1 { font-family: "Montserrat", Arial, sans-serif; font-size: 28px; font-weight: 600; text-transform: uppercase; color: var(--navy); white-space: nowrap; }
  .offer-l1 span, .offer-l4 span { color: var(--cyan); }
  .offer-l2 { font-size: 50px; margin-top: 10px; white-space: nowrap; }
  .offer-l3 { font-size: 76px; margin-top: 6px; white-space: nowrap; }
  .offer-l4 { font-family: "Montserrat", Arial, sans-serif; font-size: 28px; font-weight: 600; text-transform: uppercase; color: var(--navy); margin-top: 10px; white-space: nowrap; }
  .offer .btn { margin-top: 24px; }
  .offer-frame { left: 560px; top: 44px; width: 540px; height: 408px; background: var(--orange); }
  .offer-photo { left: 540px; top: 24px; width: 540px; height: 408px; background: linear-gradient(160deg, #0c1a3a 0%, #28336b 35%, #c2613a 60%, #1e8aa6 85%, #0d3b55 100%); }

  /* Goal band */
  .goal { height: 440px; background: var(--cyan); text-align: center; color: var(--white); }
  .goal-title { position: absolute; left: 0; width: 1200px; top: 96px; font-family: "Montserrat", Arial, sans-serif; font-size: 34px; font-weight: 700; line-height: 1.3; }
  .goal-text { position: absolute; left: 0; width: 1200px; top: 196px; font-size: 17px; line-height: 1.5; }
  .progress { left: 330px; top: 268px; width: 540px; }
  .progress-labels { display: flex; justify-content: space-between; font-family: "Montserrat", Arial, sans-serif; font-size: 11px; font-weight: 600; line-height: 1.4; text-align: center; }
  .progress-track { margin-top: 8px; height: 10px; background: rgba(255,255,255,.45); position: relative; }
  .progress-fill { position: absolute; left: 0; top: 0; height: 10px; width: 54%; background: var(--orange); }
  .progress-pct { margin-top: 8px; width: 54%; text-align: right; font-family: "Montserrat", Arial, sans-serif; font-weight: 700; font-size: 14px; }

  /* Facts */
  .facts { height: 500px; }
  .facts-photo { left: 136px; top: 44px; width: 330px; height: 330px; background: radial-gradient(circle at 50% 60%, #f1ece1 0%, #d6dde6 55%, #b9c8d6 100%); }
  .facts-status { left: 336px; top: 200px; width: 240px; height: 240px; border-radius: 50%; background: var(--orange); color: var(--white); padding: 54px 28px 0; font-family: "Montserrat", Arial, sans-serif; }
  .status-head { text-align: center; font-size: 11px; font-weight: 700; letter-spacing: .5px; }
  .status-value { text-align: center; font-size: 10px; margin-bottom: 10px; }
  .status-grid { display: grid; grid-template-columns: 1fr 1fr; gap: 8px 10px; font-size: 9px; font-weight: 600; border-top: 1px solid rgba(255,255,255,.5); padding-top: 8px; }
  .facts-copy { left: 640px; top: 104px; width: 480px; }

  .section-copy .heading { font-size: 36px; margin: 8px 0 16px; white-space: nowrap; }

  /* Climate */
  .climate { height: 540px; background: var(--cyan); }
  .climate .eyebrow, .climate .heading { color: var(--white); }
  .climate .body-copy { color: var(--white); }
  .climate-copy { left: 96px; top: 130px; width: 470px; }
  .climate-ice { left: 746px; top: 100px; width: 364px; height: 364px; background: radial-gradient(circle at 45% 40%, #e9f6fb 0%, #9fd6ee 45%, #3f99c9 100%); }
  .climate-bear { left: 680px; top: 306px; width: 218px; height: 218px; background: linear-gradient(180deg, #b9c9d4 0%, #c8b9a2 70%, #9c8a74 100%); border: 6px solid var(--cyan); }

  /* Urgency */
  .urgency { height: 540px; }
  .urgency-big { left: 160px; top: 84px; width: 300px; height: 300px; background: radial-gradient(circle at 50% 50%, #f2ede3 0%, #cfd6de 60%, #aeb9c4 100%); }
  .urgency-small { left: 340px; top: 264px; width: 224px; height: 224px; background: radial-gradient(circle at 50% 50%, #f5f2ea 0%, #dfe3e8 60%, #c2ccd6 100%); border: 6px solid var(--white); }
  .urgency-copy { left: 640px; top: 130px; width: 480px; }

  /* Quote */
  .quote { height: 540px; background: var(--cyan); text-align: center; color: var(--white); }
  .quote-avatar { left: 556px; top: 100px; width: 88px; height: 88px; background: linear-gradient(160deg, #5c4a3e 0%, #8a7565 60%, #3b3029 100%); }
  .quote-text { position: absolute; left: 0; width: 1200px; top: 226px; font-family: "Montserrat", Arial, sans-serif; font-size: 36px; font-weight: 700; line-height: 1.35; }
  .quote-cite { position: absolute; left: 0; width: 1200px; top: 338px; font-size: 19px; }
  .quote .btn { position: absolute; left: 527px; top: 388px; }

  /* Help */
  .help { height: 540px; }
  .help-copy { left: 96px; top: 148px; width: 470px; }
  .help-video { left: 640px; top: 148px; width: 468px; height: 312px; background: #050505; }
  .video-bar { left: 0; bottom: 0; width: 468px; height: 28px; background: #1b1b1b; display: flex; align-items: center; padding: 0 10px; gap: 10px; }
  .video-track { flex: 1; height: 4px; background: #555; }

  /* Cards */
  .pillars { height: 560px; background: var(--light); }
  .pillar { top: 128px; width: 316px; }
  .pillar-photo { width: 316px; height: 210px; }
  .pillar h3 { font-family: "Montserrat", Arial, sans-serif; font-size: 18px; font-weight: 700; color: var(--navy); margin: 18px 0 8px; }
  .pillar p { font-size: 13px; line-height: 1.65; }

  /* Closing CTA */
  .closing { height: 240px; background: var(--navy); text-align: center; color: var(--white); }
  .closing-title { position: absolute; left: 0; width: 1200px; top: 48px; font-family: "Montserrat", Arial, sans-serif; font-size: 34px; font-weight: 700; }
  .closing-sub { position: absolute; left: 0; width: 1200px; top: 100px; font-size: 17px; }
  .closing .btn { position: absolute; left: 527px; top: 148px; }
  .legal { height: 60px; background: var(--navy-deep); border-top: 2px solid var(--cyan); text-align: center; font-size: 11px; line-height: 58px; color: #8a95a2; }
  .legal span { color: var(--orange); }
</style>
</head>
<body>

<section class="hero">
  <div class="abs hero-bear" role="img" aria-label="Polar bear standing on snow"></div>
  <div class="abs brand"><span class="brand-mark"></span>Marlowe Bright Works</div>
  <h1 class="abs heading hero-title">The Polar Bears</h1>
  <div class="abs hero-sub">Essential Habitat</div>
  <div class="abs hero-line">Help preserve essential polar habitat</div>
  <a class="abs btn">Donate Now</a>
</section>

<section class="offer">
  <div class="abs offer-copy">
    <div class="offer-l1"><span>Donate $100</span> and receive</div>
    <div class="heading offer-l2">A Free 3 Night</div>
    <div class="heading offer-l3">Vacation</div>
    <div class="offer-l4">Certificate to <span>Las Vegas</span></div>
    <a class="btn">Donate Now</a>
  </div>
  <div class="abs offer-frame"></div>
  <div class="abs offer-photo" role="img" aria-label="Las Vegas strip at dusk with hotel towers and fountains"></div>
</section>

<section class="goal">
  <h2 class="goal-title">Donate today &amp; help us reach our $1M goal to<br>Preserve the polar bear's Arctic Home</h2>
  <p class="goal-text">Polar bears live on the ice-covered waters of the arctic, relying almost entirely on<br>drinking sea ice for their survival.</p>
  <div class="abs progress">
    <div class="progress-labels">
      <div>$0</div>
      <div>RAISED<br>$ 540,000</div>
      <div>TOTAL GOAL<br>$ 1,000,000</div>
    </div>
    <div class="progress-track"><div class="progress-fill"></div></div>
    <div class="progress-pct">54%</div>
  </div>
</section>

<section class="facts">
  <div class="abs photo facts-photo" role="img" aria-label="Polar bear mother with two cubs on snow"></div>
  <div class="abs facts-status">
    <div class="status-head">CONSERVATION STATUS</div>
    <div class="status-value">VULNERABLE</div>
    <div class="status-grid">
      <div>POPULATION<br>26,000</div>
      <div>LIFESPAN<br>25 YEARS</div>
      <div>WEIGHT<br>700 KG</div>
      <div>TOP SPEED<br>40 KM/H</div>
    </div>
  </div>
  <div class="abs section-copy facts-copy">
    <div class="eyebrow">The Facts</div>
    <h2 class="heading">The Polar Bear</h2>
    <p class="body-copy">Polar bears depend on sea ice to hunt, travel and raise their young. As the Arctic warms, the ice forms later and melts sooner each year, leaving bears with less time to feed. Every donation funds field research, habitat monitoring and local programs that protect the places these bears call home. Together we can give them a stronger future on the ice.</p>
  </div>
</section>

<section class="climate">
  <div class="abs section-copy climate-copy">
    <div class="eyebrow">The Issues</div>
    <h2 class="heading">Climate Change</h2>
    <p class="body-copy">Rising temperatures are shrinking the Arctic sea ice at a record pace. Longer open-water seasons force bears to swim farther and fast longer between meals. Our partners track these changes closely and share the data with communities and decision makers. Your gift helps turn this research into real protection for the habitat that remains.</p>
  </div>
  <div class="abs photo climate-ice" role="img" aria-label="Blue glacier ice cave"></div>
  <div class="abs photo climate-bear" role="img" aria-label="Polar bear resting on bare ground"></div>
</section>

<section class="urgency">
  <div class="abs photo urgency-big" role="img" aria-label="Polar bear walking through snow"></div>
  <div class="abs photo urgency-small" role="img" aria-label="Polar bear cubs playing in snow"></div>
  <div class="abs section-copy urgency-copy">
    <div class="eyebrow">The Urgency</div>
    <h2 class="heading">Time is running out<br>for the polar bear</h2>
    <p class="body-copy">Scientists warn that some polar bear groups could decline sharply within our lifetime. Cubs need stable ice and well-fed mothers to survive their first years. Acting now gives us the best chance to slow the loss, protect key denning areas and keep healthy populations across the North. Every dollar raised moves us closer to our goal.</p>
  </div>
</section>

<section class="quote">
  <div class="abs quote-avatar" role="img" aria-label="Portrait of the lead researcher"></div>
  <blockquote class="quote-text">“I Predict That We Could See Ice-Free<br>Summers on the North Pole Within a Decade.”</blockquote>
  <p class="quote-cite">Elena Marsh, Lead Researcher, The Northern Ice Institute</p>
  <a class="btn">Donate Now</a>
</section>

<section class="help">
  <div class="abs section-copy help-copy">
    <div class="eyebrow">The Urgency</div>
    <h2 class="heading">Help us protect<br>the Arctic</h2>
    <p class="body-copy">Protecting the Arctic means working on many fronts at once. We support research teams, partner with northern communities and push for smarter rules on shipping and industry. Watch the short film to see the work in the field and learn how your donation makes a difference today. When you give $100 you also receive a free vacation certificate.</p>
  </div>
  <div class="abs help-video" role="img" aria-label="Video about protecting the Arctic">
    <div class="abs video-bar">
      <svg width="12" height="12" viewBox="0 0 12 12"><path d="M2 1 L11 6 L2 11 Z" fill="#ddd"/></svg>
      <div class="video-track"></div>
      <svg width="14" height="12" viewBox="0 0 14 12"><path d="M1 4 H4 L8 1 V11 L4 8 H1 Z" fill="#ddd"/></svg>
    </div>
  </div>
</section>

<section class="pillars">
  <div class="abs pillar" style="left:96px">
    <div class="pillar-photo" role="img" aria-label="Industrial plant under a blue sky" style="background:linear-gradient(180deg,#6fa9d8 0%,#b8d4ea 55%,#8a9aa6 100%)"></div>
    <h3>Reducing industrial impacts</h3>
    <p>We work with industry to lower pollution, reduce spills and limit shipping noise in sensitive Arctic waters where polar bears hunt and rest.</p>
  </div>
  <div class="abs pillar" style="left:442px">
    <div class="pillar-photo" role="img" aria-label="Two people shaking hands" style="background:linear-gradient(135deg,#2e4a6b 0%,#7a8ea4 55%,#c9d2dc 100%)"></div>
    <h3>Working Together</h3>
    <p>We join with local communities, scientists and partners to share knowledge and build practical plans that keep people and bears safe.</p>
  </div>
  <div class="abs pillar" style="left:788px">
    <div class="pillar-photo" role="img" aria-label="Researchers reviewing population data" style="background:linear-gradient(135deg,#e8e4de 0%,#b89a84 50%,#3c4656 100%)"></div>
    <h3>Monitoring Population</h3>
    <p>Our teams count and track bears across the region, giving us the clear data needed to guide protection efforts year after year.</p>
  </div>
</section>

<footer class="closing">
  <h2 class="closing-title">Donate Today &amp; Help Us Reach</h2>
  <p class="closing-sub">our $1M goal to preserve the polar bear's Arctic home</p>
  <a class="btn">Donate Today</a>
</footer>
<footer class="legal">© 2015 <span>Marlowe Bright Works</span>. All Rights Reserved</footer>

</body>
</html>
```